Rigboard Media Co Business Card Design

We have a newly created business and logo, but we now need business cards using the new logo.
We are an Australian based business, and we sell advertising space on trucks. The business cards will be seen by media buyers, direct advertisers, fleet owners and business people in general.
Our colours are very simple - black and a strong yellow, with some white. We have chosen the black and yellow for various reasons, but in particular because they are high contrast, and they also have a parallel with the number plates used on our roads, which is relevant to our product offering.
My initial thoughts:
Keep it simple and uncluttered
Use both sides
Our default is Century Gothic
I can provide logo files as required. We do not yet have a website, so I can't direct you there just yet. That may well be another project!
Target Market(s)
The business cards will be seen by media buyers, direct advertisers, fleet owners and business people in general.
Industry/Entity Type
Advertising
Look and feel

```html
<!DOCTYPE html>
<html lang="en">
<head>
<meta charset="utf-8">
<title>Rigboard Media Co – Business Card</title>
<link rel="stylesheet" href="https://fonts.googleapis.com/css2?family=Marcellus+SC&display=swap">
<style>
  :root {
    --ink: #000000;
    --signal-yellow: #eeff0a;
    --paper: #ffffff;
    --steel-light: #e4e4e4;
    --steel-mid: #a9a9a9;
    --steel-dark: #3a3a3a;
    --card-font: "Marcellus SC", "Copperplate", serif;
  }
  * { box-sizing: border-box; margin: 0; padding: 0; }
  html, body {
    width: 1200px; height: 900px; overflow: hidden;
    background: var(--paper);
  }
  .canvas { position: relative; width: 1200px; height: 900px; font-family: var(--card-font); }

  /* Front side */
  .card-front {
    position: absolute; left: 78px; top: 33px; width: 718px; height: 411px;
    background: var(--ink);
  }
  .plate-frame {
    position: absolute; left: 15px; top: 21px; width: 686px; height: 369px;
    border: 29px solid var(--signal-yellow); border-radius: 36px;
    display: flex; align-items: center; justify-content: center; gap: 22px;
  }
  .brand-mark {
    width: 34px; height: 34px; background: var(--signal-yellow);
  }
  .brand-name {
    color: var(--signal-yellow); font-size: 50px; letter-spacing: 3px; line-height: 1;
  }

  /* Back side */
  .card-back {
    position: absolute; left: 376px; top: 463px; width: 718px; height: 410px;
    border: 1px solid #444;
    background: linear-gradient(to bottom, var(--paper) 0%, var(--paper) 12%, var(--steel-light) 42%, var(--steel-mid) 64%);
    color: var(--ink); text-align: center; overflow: hidden;
  }
  .contact-name { position: absolute; top: 34px; width: 100%; font-size: 34px; letter-spacing: 2px; }
  .contact-role { position: absolute; top: 78px; width: 100%; font-size: 20px; letter-spacing: 2px; }
  .contact-line { position: absolute; width: 100%; font-size: 24px; letter-spacing: 2px; }
  .contact-phone { top: 131px; }
  .contact-mobile { top: 168px; }
  .contact-email { top: 208px; font-size: 20px; }
  .band-shadow {
    position: absolute; left: 0; top: 258px; width: 100%; height: 14px;
    background: linear-gradient(to bottom, var(--steel-mid), var(--steel-dark));
  }
  .web-band {
    position: absolute; left: 0; top: 272px; width: 100%; height: 40px;
    background: var(--signal-yellow); font-size: 22px; letter-spacing: 2px; line-height: 42px;
    box-shadow: 0 3px 5px rgba(0,0,0,0.6);
  }
  .address-band {
    position: absolute; left: 0; top: 312px; width: 100%; height: 98px;
    background: linear-gradient(to bottom, #6a6a6a 0%, var(--steel-dark) 30%, var(--ink) 100%);
    color: var(--paper); font-size: 20px; letter-spacing: 1.5px; line-height: 96px;
  }
</style>
</head>
<body>
<main class="canvas">
  <section class="card-front" aria-label="Card front">
    <div class="plate-frame">
      <span class="brand-mark"></span>
      <span class="brand-name">Rigboard Media Co</span>
    </div>
  </section>

  <section class="card-back" aria-label="Card back">
    <h1 class="contact-name">Dean Harlow</h1>
    <p class="contact-role">FOUNDER</p>
    <p class="contact-line contact-phone">P: 18000RIGBD</p>
    <p class="contact-line contact-mobile">M: +61 4 1555 0192</p>
    <p class="contact-line contact-email">dean@rigboard.com.au</p>
    <div class="band-shadow"></div>
    <p class="web-band">WWW.RIGBOARD.COM.AU</p>
    <p class="address-band">PO Box 2210, Harbour Vale NSW 2099</p>
  </section>
</main>
</body>
</html>
```